Website Landing Page for Brightfall Systems

Create a custom designed website landing page for our business. Looking for a professional upscale design that incorporates our logo and logo colors into the theme. I want a standard fixed frame website, not a constant scrolling format that seems to be the trend. To start with I'm looking for more of the graphic design part, maybe a concept or theme, I don't expect to see a finished project. Not interested in generic templates or layouts.

The name of our company is Brightfall Systems and I've attached our logo below. I'd like to have the web page have the same look and feel of our logo, as well as the colors. Our company, Brightfall Systems does system design, installation, and programming, of residential and commercial Audio/Video and Automation systems. We do home theaters, lighting and building automation, video conferencing systems, security camera installations, conference rooms, projectors, distributed audio systems, and similar Technology projects. This will be a professional services/informational website. We will not sell products on this website. This website will be used to advertise our company and communicate our services to prospective customers. Having a well designed, professional and clean website is one way we want to distinguish our company from the competition.

Here are some examples of what I consider a professional well designed website
http://www.qorlamstudio.com/Work/

Last year we had our tradlo store designed (with PixelMarket) and I'm really happy with the way it turned out. You can see it at www.HolvenGearDepot.com I consider this to be a great design and looking for the same level of quality with this new website. However, do not copy or use any part of this design in this new project. This tradlo store is completely separate from our other company Brightfall Systems. I only mention this tradlo store an an example of good work.

Reason: Still going through designs.

Reason: Still working on project and have not had time to review all designs and request revisions.

Reason: Sill going through designs and requesting revisions

Reason: still going through all the submissions we received.

Target Market(s)

People interested in Audio/Video, home theaters, home automation. We do sales, system design, and programming. We typically work on larger projects with both residential and commercial customers.

Industry/Entity Type

Business

Number of Pages Required

1 page

Requirements
Must have
• Great design elements. Please use a white background. I think white goes well with our logo colors.

```html
<!DOCTYPE html>
<html lang="en">
<head>
<meta charset="utf-8">
<title>Brightfall Systems</title>
<link rel="stylesheet" href="https://fonts.googleapis.com/css2?family=Lato:wght@400;700&display=swap">
<style>
  :root {
    --brand-blue: #0a82c0;
    --brand-green: #0b8f2f;
    --ink: #555555;
    --ink-dark: #333333;
    --ring: #ececec;
    --ring-strong: #dcdcdc;
    --frame: #dedede;
    --paper: #ffffff;
  }
  * { margin: 0; padding: 0; box-sizing: border-box; }
  html, body { width: 1200px; height: 675px; overflow: hidden; background: var(--paper); }
  body { font-family: 'Lato', sans-serif; color: var(--ink); }
  .page { position: relative; width: 1200px; height: 675px; overflow: hidden; background: var(--paper); }
  .backdrop { position: absolute; left: 0; top: 0; width: 1200px; height: 675px; }

  .brand {
    position: absolute; left: 66px; top: 11px; width: 158px; height: 158px;
    display: flex; align-items: center; justify-content: center; text-align: center;
    color: var(--brand-blue); font-weight: 700; font-size: 15px; line-height: 1.15; letter-spacing: 0.5px;
  }

  .main-nav { position: absolute; top: 47px; left: 673px; display: flex; align-items: center; }
  .main-nav a {
    color: var(--ink); text-decoration: none; font-size: 17px; height: 50px;
    display: flex; align-items: center; justify-content: center;
  }
  .main-nav .is-active { width: 78px; border: 4px solid var(--ink-dark); }
  .main-nav .nav-services { margin-left: 30px; }
  .main-nav .nav-customers { margin-left: 47px; }
  .main-nav .nav-contact { margin-left: 48px; }

  .headline { position: absolute; left: 0; top: 0; font-weight: 400; }
  .headline span { position: absolute; white-space: nowrap; font-size: 59px; line-height: 1; }
  .headline .line-blue { left: 320px; top: 132px; color: var(--brand-blue); }
  .headline .line-green { left: 479px; top: 186px; color: var(--brand-green); }

  .photo { position: absolute; }
  .photo-auditorium { left: 74px; top: 279px; width: 333px; height: 211px;
    background: linear-gradient(160deg, #8a8a84 0%, #5d5f60 40%, #2f3a45 100%); }
  .photo-conference { left: 74px; top: 490px; width: 333px; height: 185px;
    background: linear-gradient(180deg, #d9d9d9 0%, #d9d9d9 14%, #7a3a26 15%, #5e2d1f 60%, #8d8a82 100%); }
  .photo-lounge { left: 794px; top: 279px; width: 332px; height: 396px;
    background: linear-gradient(165deg, #4a5662 0%, #2a3036 45%, #3e4a48 70%, #7a5232 100%); }

  .panel-frame { position: absolute; left: 373px; top: 353px; width: 453px; height: 360px; border: 6px solid var(--frame); }

  .slider-dots { position: absolute; left: 0; top: 0; }
  .slider-dots i { position: absolute; border-radius: 50%; background: var(--brand-blue); }

  .intro { position: absolute; left: 430px; top: 382px; width: 340px; }
  .intro h2 { font-size: 26px; font-weight: 700; text-align: center; color: var(--ink); margin-bottom: 15px; }
  .intro p { font-size: 15.3px; line-height: 21.4px; text-align: justify; text-align-last: center; color: var(--ink-dark); }

  .copyright {
    position: absolute; left: 1168px; top: 374px; transform: translate(-50%, -50%) rotate(-90deg);
    white-space: nowrap; font-size: 11px; color: var(--ink-dark);
  }
</style>
</head>
<body>
<div class="page">
  <svg class="backdrop" viewBox="0 0 1366 768" aria-hidden="true">
    <g fill="none" stroke="var(--ring)" stroke-width="7">
      <circle cx="165" cy="102" r="90"/>
      <circle cx="485" cy="65" r="72"/>
      <circle cx="270" cy="222" r="50"/>
      <circle cx="100" cy="318" r="80"/>
      <circle cx="760" cy="150" r="88"/>
      <circle cx="1008" cy="298" r="130"/>
      <circle cx="1222" cy="170" r="88"/>
      <circle cx="710" cy="385" r="72"/>
      <circle cx="48" cy="570" r="48"/>
      <circle cx="1325" cy="650" r="68"/>
      <circle cx="1330" cy="330" r="52"/>
    </g>
    <circle cx="455" cy="322" r="105" fill="none" stroke="var(--ring-strong)" stroke-width="7"/>
  </svg>

  <header>
    <div class="brand">BRIGHTFALL<br>SYSTEMS</div>
    <nav class="main-nav">
      <a href="#" class="is-active">Home</a>
      <a href="#" class="nav-services">Services</a>
      <a href="#" class="nav-customers">Customers</a>
      <a href="#" class="nav-contact">Contact Us</a>
    </nav>
  </header>

  <h1 class="headline"><span class="line-blue">Lorem ipsum</span><span class="line-green">dolor sit amet</span></h1>

  <div class="photo photo-auditorium" role="img" aria-label="Auditorium with tiered seating and a projection screen"></div>
  <div class="photo photo-conference" role="img" aria-label="Conference room with wood panelled walls and a display"></div>
  <div class="photo photo-lounge" role="img" aria-label="Modern bar lounge with pendant lights and stools"></div>

  <div class="panel-frame"></div>

  <div class="slider-dots" aria-hidden="true">
    <i style="left:530px;top:317px;width:23px;height:23px"></i>
    <i style="left:571px;top:320px;width:16px;height:16px"></i>
    <i style="left:611px;top:320px;width:16px;height:16px"></i>
    <i style="left:650px;top:320px;width:16px;height:16px"></i>
  </div>

  <section class="intro">
    <h2>Lorem Ipsum</h2>
    <p>Lorem ipsum dolor sit amet, consectetuer adipiscing elit. Aenean commodo ligula eget dolor. Aenean massa. Cum sociis natoque penatibus et magnis dis parturient montes, nascetur ridiculus mus. Donec quam felis, ultricies nec, pellentesque eu, pretium quis, sem. Nulla consequat massa quis enim. Donec pede justo, fringilla vel, aliquet nec, vulputate eget, arcu. In enim justo, rhoncus ut, imperdiet a, venenatis vitae, justo</p>
  </section>

  <footer class="copyright">Copyrights 2017 Brightfall Systems. All rights Reserved.</footer>
</div>
</body>
</html>
```